QLindex warden tap - styling

We have a prototyped single page application. The content is in place what we need is restyling to

- make it more user friendly
- modern look and feel
- improve accessibility features
- use our brand guidelines (screen shots attached of the full website)

Prototype is available at http://boardviewapp.examplehost.net/

Target form factor:
Primary - tablet
Secondary - desktop

Target Market(s)

Business users - not financial professionals but people working for big companies who have some limited training in the concepts

Number of Pages Required

1 page

Requirements
Must have
• Touch user interface

```html
<!DOCTYPE html>
<html lang="en">
<head>
<meta charset="utf-8">
<title>QLindex warden tap – Dashboard</title>
<link rel="stylesheet" href="https://fonts.googleapis.com/css2?family=Lato:wght@400;700;900&display=swap">
<style>
:root{
  --brand:#0d5fb0;
  --brand-light:#5aa9e6;
  --accent:#a5085f;
  --ink:#444;
  --muted:#666;
  --page:#f0f0f0;
  --panel:#fff;
  --row:#ececec;
  --grid:#999;
  --grey-bar:#8c8c8c;
  --legend-grey:#c4c4c4;
  --footer:#000;
  --loss:#8b3a3a;
}
*{box-sizing:border-box;margin:0;padding:0}
html,body{width:1200px;height:1125px;overflow:hidden;background:var(--page);font-family:'Lato',sans-serif;color:var(--ink)}
.stage{width:1280px;height:1200px;transform:scale(.9375);transform-origin:0 0;position:relative;background:var(--page)}
.site-header{position:absolute;left:0;top:0;width:1280px;height:121px;background:var(--brand)}
.brand{position:absolute;left:140px;top:40px;color:#fff;font-weight:900;font-size:34px;letter-spacing:-1px}
.client-select{position:absolute;left:876px;top:10px;width:172px;height:30px;background:#fff;border-radius:3px;font-size:14px;color:var(--loss);padding:6px 11px}
.client-select svg{position:absolute;right:10px;top:11px}
.logout{position:absolute;left:1068px;top:16px;color:#fff;font-size:16px;font-weight:700;display:flex;gap:8px;align-items:center}
.main-nav{position:absolute;left:504px;top:75px;display:flex;height:46px}
.main-nav a{color:#fff;text-decoration:none;font-size:16px;font-weight:700;padding:10px 20px 0;display:block}
.main-nav a.active{background:var(--page);color:var(--brand);padding:10px 14px 0}
.page-title{position:absolute;left:139px;top:154px;font-size:30px;color:var(--brand);font-weight:400}
.crumb{position:absolute;left:140px;top:192px;font-size:14px;color:var(--loss)}
.crumb b{color:#333;margin-right:8px}
.panel{position:absolute;background:var(--panel);border:1px solid #ddd;border-radius:3px;width:481px}
.tabs{display:flex;gap:0;font-size:14px;font-weight:700;color:var(--brand);padding:0 0 0 10px;height:36px;border-bottom:1px solid #eee}
.tabs span{padding:8px 10px 0;height:36px}
.tabs span.on{border-bottom:3px solid var(--brand)}
.tools{position:absolute;right:8px;top:9px;display:flex;gap:8px}
.panel h2{font-size:16px;font-weight:700;color:var(--brand-light);position:absolute}
.big{position:absolute;font-size:28px;font-weight:700;color:var(--brand)}
.sub{position:absolute;font-size:12px;font-weight:700;color:#444}
.legend{position:absolute;right:8px;top:54px;display:flex;gap:10px;font-size:10px;color:var(--muted);align-items:center}
.legend i{display:inline-block;width:11px;height:11px;margin-right:6px;vertical-align:-1px}
.chart{position:absolute;left:0;top:0}
.seg{position:absolute;display:flex;font-size:14px;font-weight:700}
.seg span{padding:6px 8px 3px;color:var(--loss);width:98px;text-align:center}
.seg span.on{border:1px solid var(--brand);border-bottom:none;color:var(--brand);background:#fff}
.seg-line{position:absolute;height:1px;background:var(--brand)}
table{position:absolute;border-collapse:collapse;font-size:14px;color:#555}
th{font-weight:700;color:#444;text-align:right;height:30px;padding:0 4px}
th:first-child{text-align:left}
td{height:35px;padding:0 6px;text-align:right;white-space:nowrap}
td:first-child{text-align:left}
tr.alt td{background:var(--row)}
.up{color:var(--brand)}
.arrow{font-size:11px;color:#111;width:24px;text-align:center;padding:0}
.arrow.up{color:var(--brand)}
.site-footer{position:absolute;left:0;top:1075px;width:1280px;height:125px;background:var(--footer);color:#fff;text-align:center;font-size:14px;line-height:27px;padding-top:23px}
</style>
</head>
<body>
<div class="stage">
  <header class="site-header">
    <div class="brand">QLindex</div>
    <div class="client-select">ZYX
      <svg width="9" height="6" viewBox="0 0 9 6"><path d="M1 1l3.5 3.5L8 1" stroke="#333" stroke-width="1.5" fill="none"/></svg>
    </div>
    <div class="logout">
      <svg width="16" height="16" viewBox="0 0 16 16"><circle cx="8" cy="4.5" r="3.5" fill="#fff"/><path d="M1 15c0-4 3-6 7-6s7 2 7 6z" fill="#fff"/></svg>Logout
    </div>
    <nav class="main-nav">
      <a class="active" href="#">Dashboard</a><a href="#">Analytics</a><a href="#">Risk</a><a href="#">Alm</a><a href="#">Optimizer</a><a href="#">Curves</a><a href="#">Admin</a>
    </nav>
  </header>

  <h1 class="page-title">ZYX</h1>
  <p class="crumb"><b>›</b>All Schemes, Economic basis as at August 31 2014; 1yr Monte Carlo 95% Var</p>

  <!-- Funding level -->
  <section class="panel" style="left:140px;top:245px;height:401px">
    <div class="tabs"><span>Daily</span><span class="on">Monthly</span><span>Yearly</span></div>
    <div class="tools">
      <svg width="66" height="14" viewBox="0 0 66 14" fill="#333"><path d="M7 2a5 5 0 1 0 5 5h-2a3 3 0 1 1-3-3v2l3-3-3-3z"/><circle cx="28" cy="7" r="4"/><circle cx="28" cy="7" r="1.5" fill="#fff"/><path d="M40 1h4v2h-2v2h-2zM52 1h-4v2h2v2h2zM40 13h4v-2h-2v-2h-2zM52 13h-4v-2h2v-2h2z"/><path d="M56 1h3v3h-3zM60 1h3v3h-3zM64 1h2v3h-2zM56 5h3v3h-3zM60 5h3v3h-3zM64 5h2v3h-2zM56 9h3v3h-3zM60 9h3v3h-3zM64 9h2v3h-2z"/></svg>
    </div>
    <h2 style="left:10px;top:50px">Funding Lavel</h2>
    <div class="legend">
      <span><i style="background:var(--legend-grey)"></i>Assets</span>
      <span><i style="background:var(--brand)"></i>Economic</span>
      <span><i style="background:var(--accent)"></i>Gilts 50bps</span>
      <span><i style="background:var(--brand-light)"></i>IAS19</span>
    </div>
    <div class="big" style="left:10px;top:84px">52.7%</div>
    <div class="sub" style="left:11px;top:130px">Valuation History, GBP m</div>
    <svg class="chart" width="481" height="401" viewBox="140 245 481 401" role="img" aria-label="Valuation history bar chart">
      <g font-size="11" fill="#444">
        <text x="150" y="424">1000</text><text x="150" y="461">750</text><text x="150" y="499">500</text><text x="150" y="536">250</text><text x="150" y="574">0</text>
      </g>
      <g fill="#ececec">
        <rect x="178" y="503" width="72" height="67"/><rect x="251" y="503" width="72" height="67"/><rect x="324" y="503" width="72" height="67"/><rect x="397" y="503" width="72" height="67"/><rect x="470" y="502" width="72" height="68"/><rect x="543" y="499" width="69" height="71"/>
      </g>
      <g stroke="#bbb" stroke-width="1">
        <line x1="178" y1="420" x2="612" y2="420"/><line x1="178" y1="457" x2="612" y2="457"/><line x1="178" y1="495" x2="612" y2="495"/><line x1="178" y1="532" x2="612" y2="532"/>
        <line x1="178" y1="572" x2="612" y2="572" stroke="#777"/>
      </g>
      <g>
        <g transform="translate(0,0)"><rect x="203" y="448" width="9" height="122" fill="var(--brand)"/><rect x="213" y="466" width="9" height="104" fill="var(--accent)"/><rect x="223" y="482" width="9" height="88" fill="var(--brand-light)"/></g>
        <g transform="translate(72,-1)"><rect x="203" y="448" width="9" height="123" fill="var(--brand)"/><rect x="213" y="466" width="9" height="105" fill="var(--accent)"/><rect x="223" y="481" width="9" height="90" fill="var(--brand-light)"/></g>
        <g transform="translate(144,-2)"><rect x="203" y="448" width="9" height="124" fill="var(--brand)"/><rect x="213" y="466" width="9" height="106" fill="var(--accent)"/><rect x="223" y="480" width="9" height="92" fill="var(--brand-light)"/></g>
        <g transform="translate(216,-2)"><rect x="203" y="448" width="9" height="124" fill="var(--brand)"/><rect x="213" y="467" width="9" height="105" fill="var(--accent)"/><rect x="223" y="481" width="9" height="91" fill="var(--brand-light)"/></g>
        <g transform="translate(290,-4)"><rect x="203" y="448" width="9" height="126" fill="var(--brand)"/><rect x="213" y="468" width="9" height="106" fill="var(--accent)"/><rect x="223" y="482" width="9" height="92" fill="var(--brand-light)"/></g>
        <rect x="561" y="434" width="9" height="136" fill="var(--brand)" stroke="#000" stroke-width="2"/><rect x="573" y="458" width="9" height="112" fill="var(--accent)"/><rect x="584" y="473" width="9" height="97" fill="var(--brand-light)"/>
      </g>
      <g font-size="10" fill="#555" text-anchor="middle">
        <text x="219" y="588">03/31/2014</text><text x="290" y="588">04/30/2014</text><text x="363" y="588">05/31/2014</text><text x="435" y="588">06/30/2014</text><text x="507" y="588">07/31/2014</text><text x="579" y="589" font-weight="700" fill="#222">08/31/2014</text>
      </g>
    </svg>
  </section>

  <!-- VaR -->
  <section class="panel" style="left:660px;top:245px;height:401px">
    <div class="tabs"><span>Daily</span><span>Monthly</span><span class="on">Yearly</span></div>
    <div class="tools">
      <svg width="66" height="14" viewBox="0 0 66 14" fill="#333"><path d="M7 2a5 5 0 1 0 5 5h-2a3 3 0 1 1-3-3v2l3-3-3-3z"/><circle cx="28" cy="7" r="4"/><circle cx="28" cy="7" r="1.5" fill="#fff"/><path d="M40 1h4v2h-2v2h-2zM52 1h-4v2h2v2h2zM40 13h4v-2h-2v-2h-2zM52 13h-4v-2h2v-2h2z"/><path d="M56 1h3v3h-3zM60 1h3v3h-3zM64 1h2v3h-2zM56 5h3v3h-3zM60 5h3v3h-3zM64 5h2v3h-2zM56 9h3v3h-3zM60 9h3v3h-3zM64 9h2v3h-2z"/></svg>
    </div>
    <h2 style="left:12px;top:50px">Var, 1-year Monte Carli 95 %</h2>
    <div class="big" style="left:12px;top:84px">GBP 134,930,138</div>
    <div class="sub" style="left:13px;top:130px">Risk attribution,GBP m</div>
    <svg class="chart" width="481" height="401" viewBox="660 245 481 401" role="img" aria-label="Risk attribution waterfall chart">
      <g font-size="11" fill="#444">
        <text x="673" y="424">400</text><text x="673" y="461">300</text><text x="673" y="499">200</text><text x="673" y="536">100</text><text x="673" y="574">0</text>
      </g>
      <g stroke="#999"><line x1="700" y1="418" x2="1133" y2="418"/><line x1="700" y1="457" x2="1133" y2="457"/><line x1="700" y1="494" x2="1133" y2="494"/><line x1="700" y1="532" x2="1133" y2="532"/><line x1="700" y1="572" x2="1133" y2="572" stroke="#666"/></g>
      <g fill="var(--brand)">
        <rect x="712" y="522" width="20" height="48"/><rect x="760" y="472" width="20" height="48"/><rect x="808" y="464" width="20" height="8"/><rect x="851" y="461" width="20" height="3"/><rect x="887" y="460" width="20" height="3"/><rect x="933" y="458" width="20" height="4"/><rect x="986" y="458" width="20" height="4"/>
      </g>
      <rect x="1050" y="458" width="20" height="61" fill="var(--grey-bar)"/>
      <rect x="1108" y="509" width="20" height="61" fill="var(--accent)"/>
      <g font-size="10" fill="#555" text-anchor="middle">
        <text x="720" y="590">interest</text><text x="720" y="602">rate</text><text x="771" y="590">inflation</text><text x="820" y="590">Equity</text><text x="858" y="590">FX</text><text x="897" y="590">Credit</text><text x="943" y="590">Swap</text><text x="943" y="602">Spread</text><text x="996" y="590">Property</text><text x="1062" y="590">Diversification</text><text x="1119" y="590">Net</text><text x="1119" y="602">risk</text>
      </g>
    </svg>
  </section>

  <!-- Valuation summary -->
  <section class="panel" style="left:140px;top:685px;height:350px">
    <h2 style="left:11px;top:10px">Valuation Summary, GBP</h2>
    <div class="seg" style="left:189px;top:38px"><span class="on">Combined</span><span>Liabilities</span><span>Assets</span></div>
    <div class="seg-line" style="left:11px;top:65px;width:459px"></div>
    <table style="left:11px;top:80px;width:459px">
      <tr><th style="width:180px">At 31 Aug 2014</th><th style="text-align:right;width:130px">Value</th><th>1mth Change</th><th></th></tr>
      <tr class="alt"><td>Assets</td><td>477,224,911</td><td class="up">4.3%</td><td class="arrow up">▲</td></tr>
      <tr><td>Liabilities</td><td>905,545,076</td><td>6.5%</td><td class="arrow">▲</td></tr>
      <tr class="alt"><td>Surplus / (deficit)</td><td>(428,320,164)</td><td>(35,755,698)</td><td class="arrow">▼</td></tr>
      <tr><td>Funding level</td><td>52.7%</td><td>(1.1%)</td><td class="arrow">▼</td></tr>
      <tr class="alt"><td>Interest rate hedge ratio</td><td>22.4%</td><td>(0.5%)</td><td class="arrow">▼</td></tr>
    </table>
  </section>

  <!-- Risk analysis -->
  <section class="panel" style="left:660px;top:685px;height:350px">
    <h2 style="left:11px;top:10px">Risk analysis, GBP m</h2>
    <div class="seg" style="left:270px;top:38px"><span class="on" style="width:88px">Sensitivity</span><span style="width:110px">Breakdown</span></div>
    <div class="seg-line" style="left:12px;top:65px;width:460px"></div>
    <table style="left:12px;top:80px;width:460px">
      <tr><th style="width:190px">Scenario</th><th style="width:116px">Surplus / (deficit)</th><th style="text-align:right" colspan="2">Movement</th></tr>
      <tr class="alt"><td>Base</td><td>(428.32)</td><td></td><td class="arrow"></td></tr>
      <tr><td>Equity prices, 20% decrease</td><td>(448.61)</td><td>(20.29)</td><td class="arrow">▼</td></tr>
      <tr class="alt"><td>Infiation. 1% increase</td><td>(662.81)</td><td>(234.49)</td><td class="arrow">▼</td></tr>
      <tr><td>Infiation. 1% decrease</td><td>(260.67)</td><td class="up">167.65</td><td class="arrow up">▲</td></tr>
      <tr class="alt"><td>Infiation rates. 1% increase</td><td>(279.52)</td><td class="up">148.80</td><td class="arrow up">▲</td></tr>
      <tr><td>Infiation rates. 1% decrease</td><td>(647.10)</td><td>(218.78)</td><td class="arrow">▼</td></tr>
    </table>
  </section>

  <footer class="site-footer">
    <div>Important information &nbsp;I&nbsp; User guide &nbsp;I&nbsp; What’s new &nbsp;I&nbsp; Change password</div>
    <div>You last logged in : 10/10/2014 &nbsp;2:47:59 PM</div>
    <div>© Copyright Ardent Risk 2014. Version : 2.49.12087.29781. All rights reserved.</div>
  </footer>
</div>
</body>
</html>
```